**** Web design project for VornaSoft ****

For my ICT company VornaSoft I need a website.

We design, build and host web-applications and we have our own CMS product. In the references part we want to show sample websites (thumbnails) + links.

It should look modern (WEB 2.0), rounded corners.

I want the following menu' s:
- Home
- Services
- References
- News
- About VornaSoft
- Contact

Sample websites:
See attachments
http://www.plumvest.com
http://www.gadomirbureauwerk.nl

Reason: Want to take some time for feedback and improvements.

Reason: I'm waiting for a black background, with shadow and ambient light. You'll make a good chance!

Industry/Entity Type

It Company

Requirements
Must have
• - Fixed width (1024px), should fit on an IPad2
- Language selection English/Dutch
- Twitter/Facebook/LinkedIn/RSS icons
- Footer for Terms of use and Copyrights
- Search box
- 3 (or more) boxes for information i.e. news, blog or advertisements
Nice to have
• - Footer Site Map
- Contrasting background outside borders
- wide image (rotator) (with transperant sentence block)
- Shadow

```html
<!DOCTYPE html>
<html lang="en">
<head>
<meta charset="utf-8">
<title>VornaSoft – Home</title>
<link rel="stylesheet" href="https://fonts.googleapis.com/css2?family=Noto+Sans:wght@400;700&family=Rokkitt:wght@400;500&family=Noto+Serif:ital,wght@0,700;1,400&family=Arimo:wght@700&display=swap">
<style>
:root{
  --navy:#0f2b4b;
  --sky:#c6dcef;
  --brand:#1a6fa8;
  --brand-dark:#0b5b93;
  --brand-light:#3fa9e0;
  --ink:#2b2b2b;
  --panel:#ffffff;
  --footer-bg:#e8f1fa;
  --footer-line:#9cc2e2;
  --orange:#f6a21a;
  --red:#e2401f;
}
*{box-sizing:border-box;margin:0;padding:0}
html,body{width:875px;height:1200px;overflow:hidden}
body{position:relative;font-family:"Noto Sans",Verdana,sans-serif;color:var(--ink);
  background:linear-gradient(180deg,#eaf5fb 0,#d9eef8 95px,var(--navy) 95px,#2f5680 180px,#8fb4d6 290px,var(--sky) 360px,var(--sky) 100%)}
.abs{position:absolute}
/* header */
.brand{left:110px;top:14px;display:flex;align-items:center;gap:10px}
.brand-dot{width:48px;height:48px;border-radius:50%;background:var(--brand)}
.brand-name{font-size:24px;color:#4c6a85}
.call{left:591px;top:14px;font-size:10px;color:#222}
.call strong{display:block;font-weight:400;font-size:18px;line-height:20px;color:#1b1b1b}
.flags{left:731px;top:26px;display:flex;gap:4px}
.search{left:591px;top:54px;width:178px;height:16px;border-radius:8px;background:#fff;border:1px solid #c9d6e0;font-size:9px;color:#777;padding-left:16px;line-height:14px}
.search-btn{position:absolute;right:-1px;top:-1px;width:53px;height:16px;border-radius:8px;background:linear-gradient(#3aa6e0,#0c6eae);color:#fff;font-weight:700;text-align:center;line-height:16px}
.nav{left:102px;top:82px;width:668px;height:30px;border-radius:4px;background:linear-gradient(#4bb5e8,#1586c9 55%,#0c6aa5);box-shadow:0 3px 0 #0a4f80;display:flex}
.nav a{font-family:"Arimo",Arial,sans-serif;font-weight:700;font-size:12px;color:#fff;text-decoration:none;text-align:center;line-height:30px;border-right:1px solid rgba(255,255,255,.25)}
.nav a:last-child{border:0}
/* hero */
.hero{left:102px;top:128px;width:668px;height:278px;background:#fff;border-radius:4px;padding:4px}
.hero-img{width:660px;height:270px;background:linear-gradient(120deg,#3c4f6a,#c9b3a3 40%,#eee 55%,#6f7f96 80%,#2c3d58)}
.caption{left:479px;top:277px;width:273px;height:111px;background:rgba(255,255,255,.88);padding:8px 14px}
.caption h2{font-family:"Noto Serif",Georgia,serif;font-weight:700;font-size:16.5px;color:var(--brand-dark);margin-bottom:7px}
.caption p{font-size:10.4px;line-height:15.5px;color:#111;width:240px}
/* content */
.panel{left:95px;top:420px;width:682px;height:762px;background:var(--panel);border-radius:6px}
.service{top:428px;width:212px;height:132px;border:1px solid #ddd;border-radius:4px;background:linear-gradient(#fff,#ececec);padding:9px 14px}
.service h3{font-weight:400;font-size:13.5px;color:var(--brand);text-transform:uppercase;margin-bottom:6px}
.service p{font-size:8.6px;line-height:13.6px;color:#333}
.more{display:inline-flex;align-items:center;gap:5px;margin-top:6px;height:17px;padding:0 8px 0 3px;border-radius:9px;border:1px solid #bbb;background:linear-gradient(#fff,#ddd);font-size:8px;color:#333}
.more i{width:10px;height:10px;border-radius:50%;background:#333}
.rule{left:102px;top:580px;width:668px;height:4px;background:#e6e6e6}
.welcome{left:116px;top:598px;width:456px}
.slab{font-family:"Rokkitt",Georgia,serif;font-weight:500;color:#3c556b}
.welcome h1{font-size:25px;font-weight:500}
.welcome h1 span{color:var(--brand-light)}
.welcome p{font-size:9.4px;line-height:15.7px;color:#333;margin-top:7px}
.sub{font-size:17px;color:#5b8bbd}
.apps{left:118px;top:811px;display:grid;grid-template-columns:115px 115px;font-size:9px;line-height:16.4px;color:#333}
.quote{left:366px;top:812px;width:204px;height:98px;border:1px solid #ddd;border-radius:4px;background:linear-gradient(#fff,#f0f0f0);padding:20px 12px 0 14px;font-family:"Noto Serif",Georgia,serif;font-style:italic;font-size:8.6px;line-height:14px;color:#555}
.dots{position:absolute;right:7px;top:6px;display:flex;gap:2px}
.dots b{width:6px;height:6px;background:#ddd}
.dots b:first-child{background:var(--brand-light)}
.quote-by{left:417px;top:913px;font-size:9px}
.news-head{left:595px;top:599px;width:175px;height:27px;border-radius:4px 4px 0 0;background:linear-gradient(#43aee6,#1273b5);color:#fff;font-size:13px;padding:5px 8px}
.news{left:595px;width:175px;height:58px;background:linear-gradient(#f2f2f2,#fff);padding:7px 4px 0 10px;display:flex;gap:9px}
.thumb{width:35px;height:35px;background:linear-gradient(#9ab4cf,#e9edf2);flex:none}
.news div{font-size:8.2px;line-height:11px;color:#333;white-space:nowrap}
.news b{font-weight:400;color:var(--brand)}
.news small{display:flex;justify-content:space-between;font-size:7px;margin-top:3px}
.news small em{font-style:normal;color:var(--brand);font-size:7.5px}
.view-all{left:716px;top:891px;width:50px;height:16px;border-radius:3px;background:#4d8fc8;color:#fff;font-size:9px;text-align:center;line-height:16px}
/* footer */
.footer{left:102px;top:941px;width:668px;height:233px;background:var(--footer-bg);border:1px solid var(--footer-line);border-radius:4px}
.fcol h4{font-weight:400;font-size:12.5px;color:var(--brand);margin-bottom:2px}
.fcol a{display:block;font-size:8.5px;line-height:17px;color:#4a88c2;text-decoration:none}
.social-title{left:378px;top:1085px;font-size:15px;color:var(--brand)}
.social{left:378px;top:1113px;display:flex;gap:9px}
.social span{width:21px;height:21px;border-radius:3px;background:#3b78b8}
.foot-brand{left:117px;top:1108px;width:50px;height:50px;border-radius:50%;background:var(--brand)}
.copy{left:171px;top:1157px;font-size:8.5px;color:#222}
.copy a{color:#4a88c2;text-decoration:none;margin-left:4px}
.rfq{left:584px;top:960px;width:172px;height:196px;border-radius:6px;background:linear-gradient(#bfe1f5,#7cc2ea);padding:6px 8px}
.rfq h4{font-weight:400;font-size:16px;color:#1d4f7b;margin-bottom:4px}
.rfq-body{background:#f4f9fd;height:152px;padding:6px;border-radius:2px}
.field{height:21px;background:#d7e4ee;border:1px solid #b5c8d6;margin-bottom:6px;font-size:9px;padding:4px 6px;color:#333}
.submit{position:absolute;right:19px;bottom:16px;width:41px;height:20px;border-radius:3px;background:linear-gradient(#ffc447,var(--orange));font-size:9px;font-weight:700;text-align:center;line-height:20px;color:#333}
</style>
</head>
<body>
<header>
  <div class="abs brand"><span class="brand-dot"></span><span class="brand-name">VornaSoft</span></div>
  <div class="abs call">Give us a call<strong>(555) 214-3870</strong></div>
  <div class="abs flags">
    <svg width="17" height="12" aria-label="Nederlands"><rect width="17" height="4" fill="#c8202f"/><rect y="4" width="17" height="4" fill="#fff"/><rect y="8" width="17" height="4" fill="#21468b"/></svg>
    <svg width="17" height="12" aria-label="English"><rect width="17" height="12" fill="#1f3f8a"/><rect x="6.5" width="4" height="12" fill="#fff"/><rect y="4" width="17" height="4" fill="#fff"/><rect x="7.5" width="2" height="12" fill="#c8202f"/><rect y="5" width="17" height="2" fill="#c8202f"/></svg>
  </div>
  <div class="abs search">Search<span class="search-btn">Search</span></div>
  <nav class="abs nav">
    <a style="width:98px">Home</a><a style="width:110px">Services</a><a style="width:122px">References</a><a style="width:90px">News</a><a style="width:143px">About VornaSoft</a><a style="width:105px">Contact</a>
  </nav>
</header>

<section class="abs hero"><div class="hero-img" role="img" aria-label="Photo of hands joining white puzzle pieces"></div></section>
<div class="abs caption"><h2>Lorem ipsum dolor sit amet</h2><p>Lorem ipsum dolor sit amet, consectetur adipisicing elit, sed do eiusmod tempor incididunt ut labore et dolore magna aliqua. Ut enim ad minim veniam,</p></div>

<div class="abs panel"></div>
<section class="abs service" style="left:102px"><h3>Your Service Here</h3><p>Lorem ipsum dolor sit amet, consectetur adipisicing elit, sed do eiusmod tempor incididunt ut labore et dolore magna aliqua. Ut enim ad minim veniam, quis nostrud exercitation ullamco laboris.</p><span class="more"><i></i>READ MORE</span></section>
<section class="abs service" style="left:330px"><h3>Your Service Here</h3><p>Lorem ipsum dolor sit amet, consectetur adipisicing elit, sed do eiusmod tempor incididunt ut labore et dolore magna aliqua. Ut enim ad minim veniam, quis nostrud exercitation ullamco laboris.</p><span class="more"><i></i>READ MORE</span></section>
<section class="abs service" style="left:557px"><h3>Your Service Here</h3><p>Lorem ipsum dolor sit amet, consectetur adipisicing elit, sed do eiusmod tempor incididunt ut labore et dolore magna aliqua. Ut enim ad minim veniam, quis nostrud exercitation ullamco laboris.</p><span class="more"><i></i>READ MORE</span></section>
<div class="abs rule"></div>

<section class="abs welcome">
  <h1 class="slab">Welcome to Vorna<span>Soft</span></h1>
  <p>Lorem ipsum dolor sit amet, consectetur adipisicing elit, sed do eiusmod tempor incididunt ut labore et dolore magna aliqua. Ut enim ad minim veniam, quis nostrud exercitation ullamco laboris nisi ut aliquip ex ea commodo consequat. Duis aute irure dolor in reprehenderit in voluptate velit esse cillum dolore eu fugiat nulla pariatur. Excepteur sint occaecat cupidatat non proident, sunt in culpa qui officia deserunt mollit anim id est laborum.</p>
  <p>Duis aute irure dolor in reprehenderit in voluptate velit esse cillum dolore eu fugiat nulla pariatur. Excepteur sint occaecat cupidatat non proident, sunt in culpa qui officia deserunt mollit anim id est laborum.</p>
</section>
<h2 class="abs slab sub" style="left:116px;top:782px">Web Applications</h2>
<div class="abs apps"><span>Pressfold Hosting</span><span>Pressfold Hosting</span><span>E-Commerce Hosting</span><span>E-Commerce Hosting</span><span>Forumly Hosting</span><span>Forumly Hosting</span><span>Pressfold Hosting</span><span>Pressfold Hosting</span><span>E-Commerce Hosting</span><span>E-Commerce Hosting</span><span>Forumly Hosting</span><span>Forumly Hosting</span></div>
<h2 class="abs slab sub" style="left:366px;top:782px">Our Clients Speak</h2>
<blockquote class="abs quote"><span class="dots"><b></b><b></b><b></b><b></b><b></b><b></b><b></b></span>Kelvane Studio created a script for me that is perfect. Reasonably priced, fast and accurate. I am a very happy customer and will return for services.</blockquote>
<svg class="abs" style="left:392px;top:909px" width="20" height="16"><path d="M0 0H18L18 15Z" fill="#f0f0f0" stroke="#ddd"/></svg>
<div class="abs quote-by">Marla</div>

<aside>
  <div class="abs news-head">Recent News</div>
  <div class="abs news" style="top:628px"><span class="thumb" role="img" aria-label="News thumbnail"></span><div><b>Headlines goes here</b><br>Lorem ipsum dolor sit amet,<br>consectetur adipisicing elit,<small>15-May-2012<em>READ MORE</em></small></div></div>
  <div class="abs news" style="top:694px"><span class="thumb" role="img" aria-label="News thumbnail"></span><div><b>Headlines goes here</b><br>Lorem ipsum dolor sit amet,<br>consectetur adipisicing elit,<small>15-May-2012<em>READ MORE</em></small></div></div>
  <div class="abs news" style="top:760px"><span class="thumb" role="img" aria-label="News thumbnail"></span><div><b>Headlines goes here</b><br>Lorem ipsum dolor sit amet,<br>consectetur adipisicing elit,<small>15-May-2012<em>READ MORE</em></small></div></div>
  <div class="abs news" style="top:826px"><span class="thumb" role="img" aria-label="News thumbnail"></span><div><b>Headlines goes here</b><br>Lorem ipsum dolor sit amet,<br>consectetur adipisicing elit,<small>15-May-2012<em>READ MORE</em></small></div></div>
  <div class="abs view-all">View All</div>
</aside>

<footer>
  <div class="abs footer"></div>
  <div class="abs fcol" style="left:113px;top:959px"><h4>Site Map</h4><a>Home</a><a>References</a><a>News</a><a>About VornaSoft</a><a>Contact</a></div>
  <div class="abs fcol" style="left:194px;top:959px"><h4>Services</h4><a>Lorem ipsum</a><a>Lorem ipsum</a><a>Lorem ipsum</a><a>Lorem ipsum</a><a>Lorem ipsum</a></div>
  <div class="abs fcol" style="left:275px;top:959px"><h4>Join Our Team</h4><a>Meet our Team</a><a>Join our Team</a></div>
  <div class="abs fcol" style="left:276px;top:1019px"><h4>Join Our Team</h4><a>Contact Info</a><a>Technical Support</a></div>
  <svg class="abs" style="left:370px;top:958px" width="212" height="118">
    <ellipse cx="66" cy="27" rx="64" ry="26" fill="#2b7fc4"/><path d="M40 48L38 72 70 50Z" fill="#2b7fc4"/>
    <ellipse cx="142" cy="70" rx="66" ry="32" fill="#4ab6ec" stroke="#1f86c9"/><path d="M160 98L172 116 140 100Z" fill="#4ab6ec"/>
    <text x="66" y="30" fill="#fff" font-size="9.5" text-anchor="middle" font-family="Noto Sans,sans-serif">INFO@VORNASOFT.COM</text>
    <text x="142" y="76" fill="#fff" font-size="14" font-weight="700" text-anchor="middle" font-family="Noto Sans,sans-serif">(555) 214-3870</text>
  </svg>
  <div class="abs social-title">LET'S GET SOCIAL</div>
  <div class="abs social"><span aria-label="Social link 1"></span><span aria-label="Social link 2"></span><span aria-label="Social link 3"></span><span aria-label="News feed"></span></div>
  <div class="abs foot-brand"></div>
  <div class="abs copy">© 2012 VornaSoft. All rights reserved. <a>Terms and Privacy Policy</a></div>
  <form class="abs rfq">
    <h4>Request a Quote</h4>
    <div class="rfq-body"><div class="field">Name</div><div class="field">Email</div><div class="field" style="height:54px">Description</div></div>
    <span class="submit">Submit</span>
  </form>
  <svg class="abs" style="left:700px;top:956px" width="58" height="58"><path d="M6 0H24L58 34V52Z" fill="var(--red)"/><text x="36" y="26" fill="#fff" font-size="11" font-weight="700" font-family="Noto Sans,sans-serif" transform="rotate(45 36 24)" text-anchor="middle">FREE!</text></svg>
</footer>
</body>
</html>
```